Adventure Sports Highway Sign

We are looking for a billboard that is 15 ft 6 inches wide x 9 ft tall on the top beside highway 340. Cars are usually traveling about 50-60mph through that area. We are an adventure sports company that does rafting, tubing, kayaking, canoeing, camping among other things. We have 4 check-in outposts in and around the Harpers Ferry area. We would like the billboard to be simple and not busy. We would like our logo to be prominent. Instead of "outfitters" in the bottom part of our logo, we would like it to say, "since 1972." We think that maybe this can alleviate the need for the "50+ years in the banner." The logo can be vertical or horizontal. I am attaching some sample tubing photos that we would also like to include. The whole picture does not have to be used. The logo should be the most prominent. We want to communicate the message of fun! We are open to having our website address or not. There are three companies in the immediate area. Will people google our name without the web address? We are in a time crunch to have this done. Thanks!!!

Target Market(s)

Families, people between 4 years and 60 years old

Industry/Entity Type

Adventure Sports

Requirements
Must have
• Our logo. Part or all of the tubing image.
Nice to have
• White background. Web address?
Should not have
• Hard to see.

```html
<!DOCTYPE html>
<html lang="en">
<head>
<meta charset="utf-8">
<title>Current &amp; Ridge Highway Billboard</title>
<link rel="stylesheet" href="https://fonts.googleapis.com/css2?family=Alfa+Slab+One&family=Poppins:wght@500&display=swap">
<style>
  :root {
    --navy: #2b2a86;
    --green: #0d6b3c;
    --white: #ffffff;
    --backdrop: #e9eaec;
    --photo-top: #6a9180;
    --photo-bottom: #6f99b8;
  }
  html, body {
    margin: 0;
    padding: 0;
    width: 911px;
    height: 1200px;
    overflow: hidden;
    background: var(--backdrop);
  }
  .canvas {
    position: relative;
    width: 911px;
    height: 1200px;
  }
  .billboard {
    position: absolute;
    left: 20px;
    top: 347px;
    width: 871px;
    height: 506px;
    background: var(--white);
    overflow: hidden;
    box-shadow: 0 2px 10px rgba(0,0,0,0.12);
  }
  .billboard-art {
    position: absolute;
    inset: 0;
    width: 871px;
    height: 506px;
  }
  .brand-name {
    position: absolute;
    left: 70px;
    top: 150px;
    margin: 0;
    font-family: "Alfa Slab One", serif;
    font-weight: 400;
    color: var(--navy);
    line-height: 0.95;
    font-size: 88px;
    letter-spacing: -1px;
  }
  .brand-name .line {
    display: block;
  }
  .brand-name .line-two {
    padding-left: 4px;
  }
  .tagline-pill {
    position: absolute;
    left: 106px;
    top: 360px;
    width: 304px;
    height: 50px;
    border-radius: 25px;
    background: var(--green);
    color: var(--white);
    font-family: "Poppins", sans-serif;
    font-weight: 500;
    font-size: 34px;
    line-height: 50px;
    text-align: center;
  }
  .web-address {
    position: absolute;
    left: 24px;
    top: 425px;
    width: 530px;
    display: flex;
    align-items: center;
    justify-content: center;
    gap: 12px;
    font-family: "Poppins", sans-serif;
    font-weight: 500;
    font-size: 42px;
    letter-spacing: 2px;
    color: var(--navy);
  }
  .web-address .rule {
    display: block;
    width: 52px;
    height: 3px;
    background: var(--navy);
  }
</style>
</head>
<body>
<main class="canvas">
  <section class="billboard">
    <svg class="billboard-art" viewBox="0 0 871 506" xmlns="http://www.w3.org/2000/svg">
      <defs>
        <linearGradient id="tubingPhotoTone" x1="0" y1="0" x2="0" y2="1">
          <stop offset="0" stop-color="var(--photo-top)"/>
          <stop offset="1" stop-color="var(--photo-bottom)"/>
        </linearGradient>
      </defs>
      <path class="tubing-photo" role="img"
            aria-label="Photo of a smiling woman in a life vest floating on a lime green river tube, with a wooded shoreline behind"
            fill="url(#tubingPhotoTone)"
            d="M710 0 C610 60 552 190 572 290 C588 380 640 450 700 506 L871 506 L871 0 Z"/>
      <path class="photo-swoosh" fill="var(--navy)"
            d="M566 250 C552 360 590 440 636 506 L700 506 C640 450 588 380 572 290 Z"/>
    </svg>

    <h1 class="brand-name">
      <span class="line">Current</span>
      <span class="line line-two">&amp; Ridge</span>
    </h1>
    <div class="tagline-pill">since 1972</div>
    <div class="web-address">
      <span class="rule"></span>
      <span class="url">currentridge.com</span>
      <span class="rule"></span>
    </div>
  </section>
</main>
</body>
</html>
```